Label design for high quality nutritional supplement brand

We need a new label design for our dietary supplement brand "NorlumPlus" from Germany. We sell high-quality nutritional supplements that help improve overall well-being.

All products in our range should receive the new label. You can find our current design on our homepage norlumplus-shop.example. The new design should be completely redesigned and look modern, fresh, high quality, minimalist and clean. We prefer the colors nude, green and earth tones.

The newly created label should contain our NorlumPlus logo. For this reason you will find this file attached. You will also find our current label, which needs to be renewed, in the appendix.

Colors

Designer to choose colors to be used in the design.

Requirements
Must have
• NorlumPlus logo

```html
<!DOCTYPE html>
<html lang="en">
<head>
<meta charset="utf-8">
<title>NorlumPlus Complex – Multivitamin Label</title>
<link rel="stylesheet" href="https://fonts.googleapis.com/css2?family=Montserrat:wght@400;500;600;900&family=Open+Sans:wght@400&display=swap">
<style>
  :root {
    --backdrop: #dcdce0;
    --lime: #c4c22a;
    --lime-light: #d3d14a;
    --lime-deep: #aeac1e;
    --paper: #ffffff;
    --ink: #0d0d0d;
    --logo-olive: #8f8e3a;
    --arc-grey: #c9c9c9;
  }
  * { margin: 0; padding: 0; box-sizing: border-box; }
  html, body {
    width: 1200px;
    height: 1200px;
    overflow: hidden;
    background: var(--backdrop);
  }
  .canvas {
    position: relative;
    width: 1200px;
    height: 1200px;
  }
  .label {
    position: absolute;
    left: 220px;
    top: 100px;
    width: 760px;
    height: 1000px;
    background: linear-gradient(90deg, var(--lime-deep) 0%, var(--lime) 35%, var(--lime-light) 75%, var(--lime) 100%);
    overflow: hidden;
    box-shadow: 0 10px 30px rgba(0,0,0,0.12);
  }
  .label-shapes {
    position: absolute;
    inset: 0;
    width: 760px;
    height: 1000px;
  }
  .brand-mark {
    position: absolute;
    top: 195px;
    left: 0;
    width: 100%;
    display: flex;
    justify-content: center;
    align-items: center;
    gap: 14px;
  }
  .brand-dot {
    width: 22px;
    height: 22px;
    border-radius: 50%;
    background: var(--logo-olive);
  }
  .brand-name {
    font-family: "Open Sans", sans-serif;
    font-weight: 400;
    font-size: 70px;
    color: var(--logo-olive);
    letter-spacing: -0.5px;
  }
  .product-title {
    position: absolute;
    top: 490px;
    left: 0;
    width: 100%;
    text-align: center;
    font-family: "Montserrat", sans-serif;
    font-weight: 900;
    font-size: 92px;
    color: var(--ink);
    letter-spacing: -2px;
    line-height: 1;
  }
  .product-subtitle {
    position: absolute;
    top: 604px;
    left: 0;
    width: 100%;
    text-align: center;
    font-family: "Montserrat", sans-serif;
    font-weight: 500;
    font-size: 58px;
    color: var(--ink);
    line-height: 1;
  }
  .product-type {
    position: absolute;
    top: 712px;
    left: 50%;
    transform: translateX(-50%);
    padding: 10px 34px;
    background: var(--paper);
    border-radius: 40px;
    font-family: "Montserrat", sans-serif;
    font-weight: 500;
    font-size: 48px;
    color: var(--ink);
    line-height: 1.2;
    white-space: nowrap;
  }
  .shop-url {
    position: absolute;
    top: 852px;
    left: 0;
    width: 100%;
    text-align: center;
    font-family: "Montserrat", sans-serif;
    font-weight: 500;
    font-size: 30px;
    color: var(--ink);
  }
  .base-band {
    position: absolute;
    left: 0;
    bottom: 20px;
    width: 100%;
    height: 26px;
    background: var(--ink);
    border-top: 4px solid var(--paper);
  }
  .base-strip {
    position: absolute;
    left: 0;
    bottom: 0;
    width: 100%;
    height: 20px;
    background: var(--paper);
  }
</style>
</head>
<body>
  <main class="canvas">
    <section class="label">
      <svg class="label-shapes" viewBox="0 0 760 1000" aria-hidden="true">
        <path class="label-top-bowl" fill="var(--paper)"
              d="M0,0 H760 V40 C650,70 610,430 380,450 C150,430 110,70 0,40 Z"/>
        <path class="label-arc" fill="none" stroke="var(--arc-grey)" stroke-width="5"
              d="M40,390 Q380,590 720,390"/>
      </svg>

      <div class="brand-mark">
        <span class="brand-dot"></span>
        <span class="brand-name">NorlumPlus</span>
      </div>

      <h1 class="product-title">NORLUMPLUS</h1>
      <p class="product-subtitle">Complex</p>
      <p class="product-type">Multivitamin</p>
      <p class="shop-url">www.norlumplus-shop.example</p>

      <div class="base-band"></div>
      <div class="base-strip"></div>
    </section>
  </main>
</body>
</html>
```